Organic Vegan Crispread - 100% Free of Soja

We are looking to update our labels for our current range of Crispbreads. They are all produced in Denmark, they are organic, vegan og we do not use any soy at all.

The crisp breads are high products and aimed for the gourmet market retail.

The range contains 6 different at the moment and will have 4 new types coming soon. The current six products are following:
Organic Crispbread Salt
Organic Crispbread Herbs
Organic Crispbread spices
Organic Crispbread Seaweed
Organic Crispbread Glutenfree
Organic Cripsbread Protein (Green Proteins)

The range will have to contain our logo and our name.

Measurements of Labels:
60mm wide
50mm High

Only front label design.

Target Market(s)

High End Consumers

Requirements
Must have
• Company Logo
Organic logo red (under this we need to write "DK-ØKO-472")
Organic logo Green (under this we need to write "EU / ikke EU-jordbrug")
Name
Visuel identity per type
Nice to have
• Red line throughout the range
Should not have
• No Bling Bling

```html
<!DOCTYPE html>
<html lang="en">
<head>
<meta charset="utf-8">
<title>Vedel Organic Crispbread Labels</title>
<link rel="stylesheet" href="https://fonts.googleapis.com/css2?family=Cabin+Sketch:wght@400;700&family=Josefin+Sans:wght@300;400&family=Open+Sans:wght@600;700&family=Pinyon+Script&display=swap">
<style>
  :root {
    --ink: #111111;
    --white: #ffffff;
    --salt-gold: #e2b21c;
    --salt-amber: #d49a12;
    --salt-glow: #fffbe6;
    --swoosh-gold: #d9a441;
    --leaf-green: #1e9a48;
    --forest-green: #0b6a2e;
    --herb-cream: #f3efa6;
    --herb-dots: #ece79a;
    --pill-green: #1f8f3e;
    --pill-green-soft: #4fae3d;
    --eu-green: #5aa532;
    --cert-red: #e2242b;
    --sketch-tan: #c9b98a;
  }
  * { box-sizing: border-box; margin: 0; padding: 0; }
  html, body { width: 1200px; height: 490px; overflow: hidden; background: var(--white); }
  .canvas { position: relative; width: 1200px; height: 490px; background: var(--white); }

  .label { position: absolute; top: 8px; width: 566px; height: 474px; overflow: hidden; }
  .label--salt {
    left: 38px;
    background:
      radial-gradient(ellipse 60% 55% at 78% 28%, var(--salt-glow) 0%, rgba(255,251,230,0.6) 40%, rgba(255,251,230,0) 75%),
      linear-gradient(160deg, var(--salt-amber) 0%, var(--salt-gold) 45%, #f3d44a 100%);
  }
  .label--herbs { left: 621px; width: 573px; background: var(--herb-cream); }

  .swoosh { position: absolute; inset: 0; width: 100%; height: 100%; }

  .maker-mark {
    position: absolute; top: 22px; left: 50%; transform: translateX(-50%);
    display: flex; align-items: center; gap: 8px;
  }
  .maker-mark__dot { width: 40px; height: 40px; border-radius: 50%; background: var(--leaf-green); }
  .maker-mark__name { font-family: "Josefin Sans", sans-serif; font-weight: 400; font-size: 22px; letter-spacing: 4px; color: var(--forest-green); }
  .label--herbs .maker-mark { top: 14px; }
  .label--herbs .maker-mark__dot { width: 32px; height: 32px; }
  .label--herbs .maker-mark__name { font-size: 18px; }

  .brand-name {
    position: absolute; left: 0; right: 0; text-align: center;
    font-family: "Josefin Sans", sans-serif; font-weight: 300;
    color: var(--ink); line-height: 1;
  }
  .label--salt .brand-name { top: 140px; font-size: 68px; letter-spacing: 14px; }
  .label--herbs .brand-name { top: 108px; font-size: 56px; letter-spacing: 12px; }

  .product-name { position: absolute; left: 0; right: 0; text-align: center; color: var(--ink); line-height: 1; }
  .product-name__line { display: block; }
  .label--salt .product-name { top: 208px; font-family: "Cabin Sketch", sans-serif; font-weight: 400; }
  .label--salt .product-name__line--top { font-size: 58px; }
  .label--salt .product-name__line--main { font-size: 60px; margin-top: 4px; }
  .label--herbs .product-name { top: 166px; font-family: "Pinyon Script", cursive; }
  .label--herbs .product-name__line--top { font-size: 62px; }
  .label--herbs .product-name__line--main { font-size: 62px; margin-top: -4px; }

  .soy-free {
    position: absolute; display: flex; align-items: center; justify-content: center;
    font-family: "Open Sans", sans-serif; font-weight: 700; color: var(--white);
  }
  .label--salt .soy-free {
    left: 184px; top: 338px; width: 200px; height: 38px; font-size: 19px;
    background: linear-gradient(180deg, var(--leaf-green), var(--pill-green));
  }
  .label--herbs .soy-free {
    left: 223px; top: 410px; width: 122px; height: 26px; font-size: 12.5px; font-weight: 600;
    background: linear-gradient(180deg, var(--pill-green-soft), var(--pill-green));
  }

  .herb-illustration {
    position: absolute; left: 219px; top: 272px; width: 108px; height: 136px;
    background: radial-gradient(ellipse at 50% 60%, var(--sketch-tan) 0%, rgba(201,185,138,0.35) 60%, rgba(201,185,138,0) 100%);
  }

  .cert { position: absolute; background: var(--white); display: flex; flex-direction: column; align-items: center; }
  .cert__caption { font-family: "Open Sans", sans-serif; font-weight: 600; font-size: 8px; color: #333; line-height: 1; }
  .cert--eu { padding: 4px 4px 3px; }
  .cert--eu .cert__shape { width: 100%; flex: 1; background: var(--eu-green); }
  .cert--eu .cert__caption { margin-top: 3px; }
  .label--salt .cert--eu { left: 38px; top: 374px; width: 98px; height: 68px; }
  .label--herbs .cert--eu { left: 35px; top: 376px; width: 96px; height: 66px; }

  .cert--dk { padding: 6px 6px 4px; }
  .label--salt .cert--dk { left: 400px; top: 370px; width: 125px; height: 72px; border: 2px solid var(--cert-red); }
  .label--herbs .cert--dk { left: 395px; top: 374px; width: 124px; height: 68px; }
  .cert--dk .cert__row { flex: 1; width: 100%; display: flex; align-items: center; gap: 8px; }
  .cert--dk .cert__shape { width: 40px; height: 40px; border-radius: 50%; background: var(--cert-red); }
  .cert--dk .cert__bars { flex: 1; display: flex; flex-direction: column; gap: 5px; }
  .cert--dk .cert__bar { height: 4px; background: var(--cert-red); opacity: 0.35; }
  .cert--dk .cert__caption { color: var(--cert-red); font-weight: 600; }
</style>
</head>
<body>
<main class="canvas">

  <section class="label label--salt" aria-label="Vedel Organic Crispbread Salt label">
    <svg class="swoosh" viewBox="0 0 566 474" preserveAspectRatio="none" aria-hidden="true">
      <defs>
        <linearGradient id="swoosh-green" x1="0" y1="0" x2="0" y2="1">
          <stop offset="0" stop-color="#15a046"/>
          <stop offset="1" stop-color="#0b6a2e"/>
        </linearGradient>
        <linearGradient id="swoosh-gold" x1="0" y1="0" x2="1" y2="0">
          <stop offset="0" stop-color="#f6e4b0"/>
          <stop offset="0.6" stop-color="#fff6df"/>
          <stop offset="1" stop-color="#d9a441"/>
        </linearGradient>
      </defs>
      <path d="M0 282 C150 350 350 420 566 436 L566 474 L0 474 Z" fill="url(#swoosh-gold)"/>
      <path d="M0 300 C150 368 350 434 566 452 L566 474 L0 474 Z" fill="url(#swoosh-green)"/>
    </svg>

    <div class="maker-mark">
      <span class="maker-mark__dot"></span>
      <span class="maker-mark__name">VEDEL</span>
    </div>

    <h1 class="brand-name">VEDEL</h1>
    <h2 class="product-name">
      <span class="product-name__line product-name__line--top">Organic</span>
      <span class="product-name__line product-name__line--main">Crispbread Salt</span>
    </h2>

    <p class="soy-free">100% Free of Soja</p>

    <div class="cert cert--eu">
      <span class="cert__shape"></span>
      <span class="cert__caption">EU/ikke EU-jordbrug</span>
    </div>
    <div class="cert cert--dk">
      <div class="cert__row">
        <span class="cert__shape"></span>
        <span class="cert__bars"><span class="cert__bar"></span><span class="cert__bar"></span><span class="cert__bar"></span></span>
      </div>
      <span class="cert__caption">DK-ØKO-472</span>
    </div>
  </section>

  <section class="label label--herbs" aria-label="Vedel Organic Crispbread Herbs label">
    <div class="maker-mark">
      <span class="maker-mark__dot"></span>
      <span class="maker-mark__name">VEDEL</span>
    </div>

    <h1 class="brand-name">VEDEL</h1>
    <h2 class="product-name">
      <span class="product-name__line product-name__line--top">Organic</span>
      <span class="product-name__line product-name__line--main">Crispbread Herbs</span>
    </h2>

    <div class="herb-illustration" role="img" aria-label="Sketched mortar and pestle with fresh herbs and flowers"></div>

    <p class="soy-free">100% Free of Soja</p>

    <div class="cert cert--eu">
      <span class="cert__shape"></span>
      <span class="cert__caption">EU/ikke EU-jordbrug</span>
    </div>
    <div class="cert cert--dk">
      <div class="cert__row">
        <span class="cert__shape"></span>
        <span class="cert__bars"><span class="cert__bar"></span><span class="cert__bar"></span><span class="cert__bar"></span></span>
      </div>
      <span class="cert__caption">DK-ØKO-472</span>
    </div>
  </section>

</main>
</body>
</html>
```